Re-Design Website

Task Outline:
Re- Web design with call-to-action orientated .
Task Description:
■Our Service
Our service is call Pindrove.
We are a mobile games only cross promotion and advertising platform.
■Reference WebSites
This will be few sites that is doing almost similar service
1.www.graphlune.com
2.www.quonbay.com
3.www.plovrik.net/ (japanese site, but don’t worry about the wordings.)
4.http://zentrawell.com/
■ Little Details
In a nutshell, we are advertising company for mobile games, which offer to show fullscreen ads(interstitial ads), standard banner ads, larger banner ads, icon ads and recommendation ads.
Our current site is at www.pindrove.net. (No copy write job has been done for contents yet, don’t worry about that)
Requirements:
● flat design, play well with white space ( we love the marlowpeak.com design )
● A straight to the point landing image
● All contents are fit in a 1 long page -Once scrolled down to contents. It needs to be very neat and clear on how it deliver the message through images and contents.
● Clean, simple. Reduce wordings; focus on graphic-information to intrigue response.
● We would like to reduce navigation activities and to have an outstanding Call To Action (CTA) button, which to convert user into conversion funnel (example, Learn More, to download our eBooks, Sign Up Now, Join)
● Interesting Vistogram/Chirplet button to build variability.
● Desired user experience, that able to convert information to graphical content. (Like above the fold like Zentrawell.com)
Please refer to a few reference images:
1. *upload a few sushi/ice cream/reon/images for them to use”
Pages to design
1. Landing page
2. About Us
3. Sign in & Sign Up (Must be simple and friendly)
Logo:
We are open to suggestions.
Color preference: (We open for suggestions) ---> WE ARE NOT GOING TO USE ORANGE
● color – change corporate Identity color. The background color can be darker above to fold to make it more stylish.
● 3 tone colors on a web page (something like marlwoPeak.com) → For Example (Refering to Marlow Peak : Main Color : Blue, Base Color : Gray… White, Tone Color : Green) ---> Sure you can play around with it.
● fun and energetic color tone (since we are strongly related with mobile games)
Font:
● clear typography - similar to product identity
● helvetica neue light (currently are using but we are open to suggestion)
Target Market:
● Game publisher
● Game Developer
● Partners: Advertising Agencies, (Business 2 Business)
● ASEAN Countries. ie Taiwan, Japan, China, HK...etc
Deadline:
● 31st December 2013

```html
<!DOCTYPE html>
<html lang="en">
<head>
<meta charset="utf-8">
<title>Pindrove – Landing</title>
<link rel="stylesheet" href="https://fonts.googleapis.com/css2?family=Lato:wght@300;400;700&display=swap">
<style>
  :root {
    --bg-dark: #15212a;
    --bg-mid: #3b4a4c;
    --bg-warm: #a59c84;
    --bg-light: #c8bfa6;
    --text-main: #ffffff;
    --text-soft: #f3ecd2;
    --cta-green: #5cb85c;
    --cta-green-dark: #4cae4c;
    --outline: rgba(255,255,255,0.75);
    --social-blue: #4267b2;
    --social-light: #f1f3f6;
    --social-border: #c8ccd2;
    --social-text: #333a44;
  }
  * { box-sizing: border-box; margin: 0; padding: 0; }
  html, body { width: 1200px; height: 692px; overflow: hidden; }
  body { font-family: "Lato", "Helvetica Neue", Arial, sans-serif; color: var(--text-main); }

  .hero { position: relative; width: 1200px; height: 692px; overflow: hidden; }

  .hero-photo {
    position: absolute; inset: 0;
    background:
      radial-gradient(ellipse 380px 300px at 830px 470px, rgba(150,120,95,0.55), transparent 70%),
      radial-gradient(ellipse 420px 260px at 230px 120px, rgba(200,205,190,0.28), transparent 70%),
      linear-gradient(100deg, var(--bg-dark) 0%, #1f2d33 30%, var(--bg-mid) 55%, var(--bg-warm) 80%, var(--bg-light) 100%);
  }
  .hero-photo::after {
    content: ""; position: absolute; inset: 0;
    background: linear-gradient(180deg, rgba(0,0,0,0.05) 0%, rgba(0,0,0,0.25) 100%);
  }

  .social-bar { position: absolute; top: 23px; left: 832px; display: flex; align-items: center; gap: 4px; font-size: 12px; font-weight: 700; }
  .social-btn { height: 23px; padding: 0 7px; display: flex; align-items: center; border-radius: 3px; }
  .social-btn--primary { background: var(--social-blue); color: #fff; }
  .social-btn--light { background: var(--social-light); color: var(--social-text); border: 1px solid var(--social-border); margin-left: 36px; }
  .social-count { height: 23px; padding: 0 5px; display: flex; align-items: center; background: #fff; color: var(--social-text); border: 1px solid var(--social-border); border-radius: 2px; font-weight: 400; }

  .brand { position: absolute; left: 69px; top: 202px; display: flex; align-items: center; gap: 22px; }
  .brand-mark { width: 74px; height: 74px; background: var(--text-main); border-radius: 12px; }
  .brand-name { font-size: 54px; font-weight: 400; color: var(--text-main); letter-spacing: 0.5px; }

  .tagline { position: absolute; left: 61px; top: 326px; font-size: 33px; font-weight: 300; line-height: 46px; }
  .tagline-line { display: block; color: var(--text-main); }
  .tagline-line--soft { color: var(--text-soft); }

  .cta-group { position: absolute; left: 61px; top: 463px; display: flex; gap: 16px; }
  .cta { height: 56px; display: flex; align-items: center; justify-content: center; font-size: 18px; font-weight: 300; text-transform: uppercase; text-decoration: none; border-radius: 4px; color: var(--text-main); }
  .cta--outline { width: 196px; border: 1px solid var(--outline); }
  .cta--solid { width: 141px; background: var(--cta-green); border: 1px solid var(--cta-green-dark); }
</style>
</head>
<body>
  <main class="hero">
    <div class="hero-photo" role="img" aria-label="Blurred photo of a hand holding a smartphone showing a mobile game ad, with a computer monitor in the background"></div>

    <div class="social-bar">
      <span class="social-btn social-btn--primary">Like</span>
      <span class="social-btn social-btn--primary">Share</span>
      <span class="social-count">234k</span>
      <span class="social-btn social-btn--light">Chirplet</span>
      <span class="social-count">1</span>
    </div>

    <div class="brand">
      <span class="brand-mark"></span>
      <span class="brand-name">pindrove</span>
    </div>

    <h1 class="tagline">
      <span class="tagline-line">Get ready to see something awesome</span>
      <span class="tagline-line tagline-line--soft">That'll change your life.</span>
    </h1>

    <div class="cta-group">
      <a class="cta cta--outline" href="#">Discover More</a>
      <a class="cta cta--solid" href="#">Subscribe</a>
    </div>
  </main>
</body>
</html>
```